Livestock Consulting Company has a logo but needs business cards and a uniform logo

My company works with farmers advising them on managing cattle and sheep. I have a logo but need business cards and a version of my logo to go onto my work shirts. I need the following wording added to my logo for my shirts "Marlowby Livestock Consulting".

```html
<!DOCTYPE html>
<html lang="en">
<head>
<meta charset="utf-8">
<title>Marlowby Livestock Consulting – Business Cards</title>
<link rel="stylesheet" href="https://fonts.googleapis.com/css2?family=Cinzel:wght@500;600&family=Arimo&family=Jost:wght@400&display=swap">
<style>
  :root {
    --stage: #2a2a2a;
    --brown: #7f6448;
    --paper: #ffffff;
    --ink: #111111;
  }
  * { margin: 0; padding: 0; box-sizing: border-box; }
  html, body { width: 1075px; height: 1200px; overflow: hidden; background: var(--stage); }
  .canvas { position: relative; width: 1075px; height: 1200px; }
  .card {
    position: absolute;
    width: 660px; height: 392px;
    border-radius: 22px;
    overflow: hidden;
    background: var(--brown);
    box-shadow: 3px 3px 0 #000;
  }
  .card--front { left: 208px; top: 189px; }
  .card--back  { left: 206px; top: 640px; }
  .card__shape { position: absolute; inset: 0; }
  .brand {
    position: absolute; left: 0; right: 0;
    display: flex; align-items: center; justify-content: center; gap: 16px;
    color: var(--paper);
    font-family: "Cinzel", serif; font-weight: 500;
  }
  .card--front .brand { top: 48px; }
  .card--back .brand { top: 138px; }
  .brand__dot { width: 30px; height: 30px; border-radius: 50%; background: var(--paper); }
  .brand__name { font-size: 23px; line-height: 1.1; letter-spacing: 0.5px; }
  .brand__name span { display: block; font-size: 13px; letter-spacing: 8px; text-align: center; }
  .person { position: absolute; left: 0; right: 0; top: 222px; text-align: center; }
  .person__name { font-family: "Cinzel", serif; font-weight: 600; font-size: 29px; color: var(--brown); line-height: 1; }
  .person__role { font-family: "Arimo", sans-serif; font-size: 16px; color: var(--ink); margin-top: 4px; }
  .contact { font-family: "Arimo", sans-serif; font-size: 17px; color: var(--ink); line-height: 23.5px; position: absolute; top: 284px; }
  .contact--address { right: 352px; text-align: right; }
  .contact--lines { left: 352px; }
  .contact__divider { position: absolute; left: 330px; top: 288px; width: 1px; height: 61px; background: #444; }
  .contact__row { display: flex; align-items: center; gap: 6px; white-space: nowrap; }
  .contact__row svg { width: 16px; height: 16px; fill: var(--brown); flex: none; }
  .accent { color: var(--brown); }
  .back-web {
    position: absolute; left: 0; right: 0; top: 347px; text-align: center;
    font-family: "Jost", sans-serif; font-size: 18px; letter-spacing: 1px; color: var(--brown);
  }
</style>
</head>
<body>
<main class="canvas">
  <section class="card card--front">
    <svg class="card__shape" viewBox="0 0 660 392" aria-hidden="true">
      <path d="M0,274 C120,110 540,110 660,274 L660,392 L0,392 Z" fill="var(--paper)"/>
    </svg>
    <div class="brand">
      <div class="brand__dot"></div>
      <div class="brand__name">Marlowby Livestock<span>Consulting</span></div>
    </div>
    <div class="person">
      <div class="person__name">CALLUM WHITFIELD</div>
      <div class="person__role">Managing Director</div>
    </div>
    <div class="contact contact--address">18, Hollins Lane<br>Tarrowfield 45452<br>Northmoor</div>
    <div class="contact__divider"></div>
    <div class="contact contact--lines">
      <div class="contact__row">
        <svg viewBox="0 0 24 24"><path d="M6.6 10.8a15.1 15.1 0 0 0 6.6 6.6l2.2-2.2c.3-.3.7-.4 1-.2 1.1.4 2.3.6 3.6.6.6 0 1 .4 1 1V20c0 .6-.4 1-1 1A17 17 0 0 1 3 4c0-.6.4-1 1-1h3.5c.6 0 1 .4 1 1 0 1.3.2 2.5.6 3.6.1.3 0 .7-.2 1z"/></svg>
        <span>044-208 317 546</span>
      </div>
      <div class="contact__row">
        <svg viewBox="0 0 24 24"><path d="M2 5h20v14H2z M3 6l9 7 9-7" stroke="#fff" stroke-width="1.5"/></svg>
        <span>info@marlowbyconsult.com</span>
      </div>
      <div class="contact__row">
        <svg viewBox="0 0 24 24"><circle cx="12" cy="12" r="9" fill="none" stroke="var(--brown)" stroke-width="2"/><path d="M3 12h18M12 3c3 3 3 15 0 18M12 3c-3 3-3 15 0 18" fill="none" stroke="var(--brown)" stroke-width="1.5"/></svg>
        <span>www.<span class="accent">marlowbyconsult</span>.com</span>
      </div>
    </div>
  </section>

  <section class="card card--back">
    <svg class="card__shape" viewBox="0 0 660 392" aria-hidden="true">
      <path d="M48,392 C150,280 510,280 614,392 Z" fill="var(--paper)"/>
    </svg>
    <div class="brand">
      <div class="brand__dot"></div>
      <div class="brand__name">Marlowby Livestock<span>Consulting</span></div>
    </div>
    <div class="back-web">WWW.MARLOWBYCONSULT.COM</div>
  </section>
</main>
</body>
</html>
```